We would like to incorporate our logo into letterhead design and envelopes. We are looking for something that is moderately conservative but not old law firm style. Both the envelopes and the letterhead must have both firm addresses. We would like to incorporate the color of the logo, but only a small amount of color - perhaps on one of the borders. The addresses for the firm locations are listed below. Given that it is a law firm, it needs to somewhat conservative, but not the old school, small black font on cream colored paper design.

The firm addresses are:

27815 N. Harlow Pemberton Pkwy.
Ste 4200
Scottsdale, AZ 85391

6100 W. Cedar Avenue
Ste 700
Burbank, CA 91623

Industry/Entity Type

Legal

Colors

Designer to choose colors to be used in the design.

Requirements
Must have
• Both addresses:
• 27815 N. Harlow Pemberton Pkwy.
• Ste 4200
• Scottsdale, AZ 85391
• 6100 W. Cedar Avenue
• Ste 700
• Burbank, CA 91623
Nice to have
• Small amount of color on border(s) that matches the logo but not too much color

```html
<!DOCTYPE html>
<html lang="en">
<head>
<meta charset="utf-8">
<title>Calloway Law — Stationery</title>
<link rel="stylesheet" href="https://fonts.googleapis.com/css2?family=Cinzel:wght@400&family=Lato:ital@1&family=Open+Sans:wght@400&display=swap">
<style>
  :root {
    --ink: #302b69;
    --rule: #2a2563;
    --paper: #f4f4f4;
    --canvas: #ffffff;
    --title: #1d3c4c;
    --text: #1a1a1a;
    --shadow: rgba(0, 0, 0, 0.45);
  }
  html, body {
    margin: 0;
    padding: 0;
    overflow: hidden;
  }
  body {
    width: 1200px;
    height: 834px;
    position: relative;
    background: var(--canvas);
  }
  .sheet-title {
    position: absolute;
    top: 28px;
    left: 0;
    width: 1200px;
    margin: 0;
    text-align: center;
    font: 400 20px "Open Sans", sans-serif;
    color: var(--title);
    letter-spacing: 0.3px;
  }
  .firm-name {
    position: absolute;
    left: 0;
    width: 100%;
    margin: 0;
    text-align: center;
    font-family: "Cinzel", serif;
    font-weight: 400;
    color: var(--ink);
    line-height: 1;
    white-space: nowrap;
  }
  .address {
    position: absolute;
    margin: 0;
    font: italic 10.5px/1.25 "Lato", sans-serif;
    color: var(--text);
    text-align: center;
    font-style: italic;
  }

  /* Letterhead */
  .letterhead {
    position: absolute;
    left: 28px;
    top: 91px;
    width: 547px;
    height: 709px;
    background: var(--paper);
    box-shadow: 3px 3px 6px var(--shadow);
  }
  .letterhead .top-band {
    position: absolute;
    top: 0;
    left: 33px;
    width: 480px;
    height: 6px;
    background: var(--rule);
  }
  .letterhead .firm-name { top: 22px; font-size: 45px; }
  .letterhead .bottom-band {
    position: absolute;
    left: 0;
    bottom: 0;
    width: 100%;
    height: 8px;
    background: var(--rule);
  }
  .letterhead .footer-tick {
    position: absolute;
    bottom: 12px;
    width: 1px;
    height: 22px;
    background: #777;
  }
  .letterhead .tick-left { left: 34px; }
  .letterhead .tick-right { right: 32px; }
  .letterhead .address-left { left: 38px; bottom: 12px; }
  .letterhead .address-right { right: 38px; bottom: 12px; }

  /* Envelope front */
  .envelope-front {
    position: absolute;
    left: 596px;
    top: 101px;
    width: 576px;
    height: 287px;
    background: var(--paper);
    box-shadow: 3px 3px 6px var(--shadow);
  }
  .envelope-front .frame {
    position: absolute;
    inset: 8px 10px 8px 10px;
    border: 1.5px solid var(--rule);
  }
  .envelope-front .firm-name { top: 26px; font-size: 34px; }
  .envelope-front .address-left { left: 20px; bottom: 20px; }
  .envelope-front .address-right { right: 20px; bottom: 20px; }

  /* Envelope back */
  .envelope-back {
    position: absolute;
    left: 596px;
    top: 500px;
    width: 573px;
    height: 287px;
    background: var(--paper);
    box-shadow: 3px 3px 6px var(--shadow);
  }
  .envelope-back .flap {
    position: absolute;
    top: 0;
    left: 0;
  }
  .envelope-back .firm-name { top: 107px; font-size: 34px; }
</style>
</head>
<body>
  <h1 class="sheet-title">Law Firm Stationary Design</h1>

  <section class="letterhead" aria-label="Letterhead">
    <div class="top-band"></div>
    <p class="firm-name">CALLOWAY LAW</p>
    <span class="footer-tick tick-left"></span>
    <span class="footer-tick tick-right"></span>
    <p class="address address-left">27815 N. Harlow Pemberton Pkwy. Ste 4200, Scottsdale,<br>AZ 85391</p>
    <p class="address address-right">6100 W. Cedar Avenue Ste 700, Burbank,<br>CA 91623</p>
    <div class="bottom-band"></div>
  </section>

  <section class="envelope-front" aria-label="Envelope front">
    <div class="frame"></div>
    <p class="firm-name">CALLOWAY LAW</p>
    <p class="address address-left">27815 N. Harlow Pemberton Pkwy. Ste 4200, Scottsdale,<br>AZ 85391</p>
    <p class="address address-right">6100 W. Cedar Avenue Ste 700, Burbank,<br>CA 91623</p>
  </section>

  <section class="envelope-back" aria-label="Envelope back">
    <svg class="flap" width="573" height="100" viewBox="0 0 573 100" aria-hidden="true">
      <path d="M0 0 L573 0 L345 78 Q286 98 227 78 Z" fill="var(--rule)"/>
    </svg>
    <p class="firm-name">CALLOWAY LAW</p>
  </section>
</body>
</html>
```